Top Producing Realtor Business Card Design

Looking for branding with my logo on all of my materials. I am a top producing real estate agent, selling expensive homes in California. I'm looking for a classy design that includes my existing logo, the company corporate logo and my photo.

Looking forward to your submissions! Thank you so much! :)

I appreciate your submissions very much!  Excellent work!  I have revised the brief to be more clear about what I think I'm looking for.  Keep the submissions coming in!!  Thank you so much :)

Target Market(s)

Wealthy home buyers and sellers in California.

Industry/Entity Type

Real Estate

Requirements
Must have
• Must include:

Homestead Pinnacle Logo

Below Homestead Pinnacle Logo it must say: Brennmoor (Helvetica font)

Complete address: 58317 Barwick Street
Brennmoor, KT 94687

Phone number: 415.962.3057 cell
415.740.2195 VM 5821 office

My photo

My name: Mara Quinlow (please make sure it's correct before you submit) :)

My MQ Logo (if possible please keep logo colors the same)

"Realtor" with a reserved symbol after or below my name

My license number: StaREB #07428915

My website: www.MaraQuinlow-example.com

My email: Mara@MaraQuinlow-example.com

Nice to have
• I'm open minded :) The main goal is to have the MQ logo is on all of my material. For the business cards I sort of imagine my MQ logo in the background, and I like a fade. I prefer the logo to be on the front of the card, and I like it on the back of the card too, So a two sided business card is ok.

I prefer the light blue Homestead Pinnacle Logo submitted. Please note the light blue color must closely match :)

Another idea is the business card can be in the format of the yard sign photo submitted (maybe changed into the light blue color), to possibly be a business card that looks like the yard sign. The yard sign layout must closely match the example submitted due to corporate guidelines.

Basically I'm looking for something that will tie everything together with my photo and logo so it's well branded in the clients mind. :)

Should not have
• Please keep the logo's exactly as they are, including color...no need to change.

If you choose to use the yard sign example provided for the business card, Please do not change the basic layout of the yard sign submitted, I have to follow the corporate standards.

```html
<!DOCTYPE html>
<html lang="en">
<head>
<meta charset="utf-8">
<title>Mara Quinlow – Business Card</title>
<link rel="stylesheet" href="https://fonts.googleapis.com/css2?family=Arimo:ital,wght@0,400;0,700;1,400&family=Roboto+Condensed:wght@400&family=Montserrat:wght@500;700&display=swap">
<style>
  :root {
    --page-bg: #e6e7e9;
    --sky-blue: #4f80c4;
    --navy-light: #1f3c7c;
    --navy-dark: #0b1740;
    --back-top: #030a1e;
    --back-bottom: #0b2c6a;
    --silver: #c9ccd3;
    --silver-dark: #8d929c;
    --mono-tint: #8f97bf;
    --white: #ffffff;
    --ink-light: #e8ecf5;
  }
  * { box-sizing: border-box; margin: 0; padding: 0; }
  html, body { width: 1200px; height: 1200px; overflow: hidden; background: var(--page-bg); }
  .canvas { position: relative; width: 1200px; height: 1200px; }

  .card {
    position: absolute; top: 210px; width: 446px; height: 783px; overflow: hidden;
    box-shadow: 6px 8px 10px rgba(0,0,0,0.28);
  }
  .card--front { left: 150px; background: linear-gradient(90deg, var(--navy-light) 0%, #142a63 45%, var(--navy-dark) 100%); }
  .card--back { left: 615px; background: linear-gradient(180deg, var(--back-top) 0%, #071b48 45%, var(--back-bottom) 100%); }

  .front-shapes { position: absolute; inset: 0; }

  .brokerage-mark {
    position: absolute; left: 35px; top: 40px; width: 157px; height: 88px;
    display: flex; align-items: center; justify-content: center; text-align: center;
    font-family: Arimo, Helvetica, sans-serif; font-weight: 700; font-size: 19px; line-height: 1.15;
    color: var(--white);
  }
  .brokerage-city {
    position: absolute; left: 35px; top: 134px; width: 157px; text-align: center;
    font-family: Arimo, Helvetica, sans-serif; font-size: 15px; color: var(--white); letter-spacing: 0.3px;
  }
  .contact-block {
    position: absolute; left: 207px; top: 38px;
    font-family: "Roboto Condensed", Arial, sans-serif; font-style: normal;
    font-size: 16px; line-height: 24.5px; color: var(--white);
  }

  .portrait {
    position: absolute; left: 110px; top: 183px; width: 225px; height: 252px; border-radius: 24px;
    background: radial-gradient(ellipse at 50% 35%, #9a9a9a 0%, #6e6e6e 55%, #3d3d3d 100%);
    border: 2px solid #2a2f3e;
  }

  .agent-name {
    position: absolute; left: 0; width: 100%; top: 440px; text-align: center;
    font-family: Arimo, Helvetica, sans-serif; font-weight: 700; font-size: 33px; letter-spacing: 0.5px;
    color: var(--silver);
  }
  .agent-title {
    position: absolute; left: 0; width: 100%; top: 478px; text-align: center;
    font-family: Arimo, Helvetica, sans-serif; font-size: 19px; color: var(--white);
  }
  .agent-title sup, .back-title sup { font-size: 0.55em; }

  .monogram {
    position: absolute; left: 0; width: 100%; text-align: center;
    font-family: Arimo, Helvetica, sans-serif; font-weight: 700;
  }
  .monogram--front { top: 520px; font-size: 92px; color: var(--mono-tint); }

  .web-links {
    position: absolute; left: 0; width: 100%; top: 651px; text-align: center;
    font-family: Arimo, Helvetica, sans-serif; font-style: italic; font-size: 19.5px; line-height: 29px; color: var(--ink-light);
  }
  .license-badge {
    position: absolute; left: 148px; top: 718px; width: 150px; height: 26px; border-radius: 7px;
    background: linear-gradient(180deg, #e4e6ea, var(--silver-dark));
    font-family: "Roboto Condensed", Arial, sans-serif; font-size: 16px; line-height: 26px; text-align: center; color: #111;
  }

  .monogram--back { top: 285px; font-size: 110px; color: var(--ink-light); }
  .back-name {
    position: absolute; left: 0; width: 100%; top: 433px; text-align: center;
    font-family: Montserrat, Arial, sans-serif; font-weight: 700; font-size: 28px; color: var(--white);
  }
  .back-title {
    position: absolute; left: 0; width: 100%; top: 469px; text-align: center;
    font-family: Montserrat, Arial, sans-serif; font-weight: 500; font-size: 18px; letter-spacing: 1px; color: var(--white);
  }
</style>
</head>
<body>
<main class="canvas">
  <section class="card card--front">
    <svg class="front-shapes" width="446" height="783" viewBox="0 0 446 783">
      <defs>
        <linearGradient id="swoosh" x1="0" x2="1" y1="0" y2="0">
          <stop offset="0" stop-color="#a9adb6"/>
          <stop offset="0.4" stop-color="#ffffff"/>
          <stop offset="1" stop-color="#b4b8c0"/>
        </linearGradient>
      </defs>
      <path d="M0 0 H446 V300 Q300 250 120 250 Q50 250 0 262 Z" fill="url(#swoosh)"/>
      <path d="M0 0 H446 V282 Q300 232 120 236 Q50 238 0 248 Z" fill="var(--sky-blue)"/>
    </svg>

    <div class="brokerage-mark">Homestead<br>Pinnacle</div>
    <div class="brokerage-city">BRENNMOOR</div>
    <address class="contact-block">
      58317 Barwick Street,<br>
      Brennmoor, KT 94687<br>
      Phone: 415.962.3057<br>
      Cell: 415.740.2195<br>
      VM 5821 office
    </address>

    <div class="portrait" role="img" aria-label="Portrait photo of the agent"></div>

    <h1 class="agent-name">MARA QUINLOW</h1>
    <p class="agent-title">Realtor <sup>®</sup></p>
    <div class="monogram monogram--front">MQ</div>

    <p class="web-links">www.MaraQuinlow-example.com<br>Mara@MaraQuinlow-example.com</p>
    <div class="license-badge">StaREB #07428915</div>
  </section>

  <section class="card card--back">
    <div class="monogram monogram--back">MQ</div>
    <h2 class="back-name">Mara Quinlow</h2>
    <p class="back-title">REALTOR<sup>®</sup></p>
  </section>
</main>
</body>
</html>
```